Saffron Vale signage

Simple design for a new food court outlet: Saffron Vale
They serve a fusion of Indian and Mediterranean food and we need signage with fonts and colors that reflect the warmth and spice of the cultures.
The sign is long and skinny. 1 foot tall by 18 feet long.

Target Market(s)

Ski resort guests eating at our base area food court with multiple selections to choose from.

Industry/Entity Type

Court

Requirements
Must have
• Clear readability. Name should be prominent and bright.
Nice to have
• Simple clear text. Possibly use fonts that relate to Indian and Mediterranean inspirations. Warm colors that make you want to eat the food.
Should not have
• Should not have too many graphic elements that it makes it hard to read.

```html
<!DOCTYPE html>
<html lang="en">
<head>
<meta charset="utf-8">
<title>Saffron Vale Signage</title>
<link rel="stylesheet" href="https://fonts.googleapis.com/css2?family=Alfa+Slab+One&family=Bree+Serif&display=swap">
<style>
  :root {
    --page: #ffffff;
    --spice-red: #8e1b1b;
    --deep-red: #6e1212;
    --saffron: #f6a51d;
    --gold: #fbc73a;
    --cream: #f2eadb;
    --outline: #3a130a;
  }
  html, body {
    margin: 0;
    padding: 0;
    width: 1200px;
    height: 900px;
    overflow: hidden;
    background: var(--page);
  }
  .canvas {
    position: relative;
    width: 1200px;
    height: 900px;
  }
  .sign {
    position: absolute;
    left: 0;
    width: 1200px;
    display: block;
  }
  .sign--slim { top: 250px; height: 130px; }
  .sign--tall { top: 406px; height: 240px; }
  .sign-name {
    font-family: "Alfa Slab One", serif;
    fill: var(--cream);
    stroke: var(--outline);
    paint-order: stroke;
    stroke-linejoin: round;
  }
  .sign-name--shadow,
  .sign-cuisine--shadow {
    fill: var(--outline);
    stroke: var(--outline);
  }
  .sign-cuisine {
    font-family: "Bree Serif", serif;
    font-weight: 700;
    fill: var(--cream);
    stroke: var(--outline);
    paint-order: stroke;
    stroke-linejoin: round;
  }
</style>
</head>
<body>
<div class="canvas">

  <svg class="sign sign--slim" viewBox="0 0 1200 130" xmlns="http://www.w3.org/2000/svg">
    <defs>
      <radialGradient id="slim-glow" cx="50%" cy="50%" r="60%" gradientTransform="translate(0.5 0.5) scale(1 3.5) translate(-0.5 -0.5)">
        <stop offset="0" stop-color="#c2461c"/>
        <stop offset="0.35" stop-color="#a52a1c"/>
        <stop offset="1" stop-color="var(--spice-red)"/>
      </radialGradient>
    </defs>
    <rect class="sign-backdrop" width="1200" height="130" fill="url(#slim-glow)" role="img" aria-label="Warm sunburst rays radiating from the centre"/>
    <text class="sign-name sign-name--shadow" x="603" y="72" text-anchor="middle" font-size="54" stroke-width="6">SAFFRON VALE</text>
    <text class="sign-name" x="600" y="68" text-anchor="middle" font-size="54" stroke-width="6">SAFFRON VALE</text>
    <text class="sign-cuisine sign-cuisine--shadow" x="602" y="118" text-anchor="middle" font-size="34" stroke-width="5">Mediterranean &amp; Indian</text>
    <text class="sign-cuisine" x="600" y="115" text-anchor="middle" font-size="34" stroke-width="5">Mediterranean &amp; Indian</text>
  </svg>

  <svg class="sign sign--tall" viewBox="0 0 1200 240" xmlns="http://www.w3.org/2000/svg">
    <defs>
      <radialGradient id="tall-glow" cx="50%" cy="50%" r="55%" gradientTransform="translate(0.5 0.5) scale(1 5) translate(-0.5 -0.5)">
        <stop offset="0" stop-color="var(--gold)"/>
        <stop offset="0.45" stop-color="var(--saffron)"/>
        <stop offset="0.8" stop-color="#c1431c"/>
        <stop offset="1" stop-color="var(--spice-red)"/>
      </radialGradient>
    </defs>
    <rect class="sign-backdrop" width="1200" height="240" fill="url(#tall-glow)" role="img" aria-label="Saffron and red sunburst rays radiating from the centre"/>
    <text class="sign-name sign-name--shadow" x="606" y="140" text-anchor="middle" font-size="104" stroke-width="12">SAFFRON VALE</text>
    <text class="sign-name" x="600" y="134" text-anchor="middle" font-size="104" stroke-width="12">SAFFRON VALE</text>
    <text class="sign-cuisine sign-cuisine--shadow" x="604" y="222" text-anchor="middle" font-size="68" stroke-width="9">Mediterranean &amp; Indian</text>
    <text class="sign-cuisine" x="600" y="218" text-anchor="middle" font-size="68" stroke-width="9">Mediterranean &amp; Indian</text>
  </svg>

</div>
</body>
</html>
```